Orbel Appraisals website redesign

I would like to refresh my existing website of www.orbelappraisals-demo.com with new graphics, look and feel, as well as updated structure and wording. Content and layout changes have been uploaded to this project Brief.

My existing website has a dark feel. I am now looking for a light and energetic feel. Financial Services is my industry, so the website should be reflect that. I would also like to reflect the concepts of Trust, Service and Expertise.

The website must be serious and upmarket.

Target Market(s)

Corporate board members, CFO's, treasurers and controllers
Auditors, tax advisors, private equity and venture capital asset managers, investors, tax authorities

Industry/Entity Type

Financial Service

Coding

Coded - Design and coding required

Number of Pages Required

5+ page

Font styles to use
Sans Serif
Other font styles liked:
• Designer can choose another modern font

Colors
0355a3
3277b5
85acd3
eaf1f7
f37122
f68d4d
9bcb3c
acd037
cadf82

Requirements
Must have
• Good hi resolution pictures that convey "Finance", "Trust", "Service" or "Expertise".
• An anti-bot (such as Captcha) mechanism in the contact form.
Should not have
• Must not have all content on one rolling screen.

```html
<!DOCTYPE html>
<html lang="en">
<head>
<meta charset="utf-8">
<title>Orbel Appraisals — Business and Intellectual Property Valuation</title>
<link href="https://fonts.googleapis.com/css2?family=Nunito+Sans:wght@400;600;700&display=swap" rel="stylesheet">
<style>
:root{
  --blue-deep:#0355a3;
  --blue:#3277b5;
  --blue-soft:#85acd3;
  --blue-pale:#eaf1f7;
  --orange:#f37122;
  --orange-soft:#f68d4d;
  --ink:#1a1a1a;
  --text:#444;
  --white:#fff;
  --arrow-blue:#2d8ff0;
}
*{margin:0;padding:0;box-sizing:border-box}
html,body{width:1200px;height:2204px;overflow:hidden;background:var(--white)}
body{position:relative;font-family:"Nunito Sans",sans-serif;color:var(--ink)}
.abs{position:absolute}

/* header */
.site-header{position:absolute;left:0;top:0;width:1200px;height:74px;background:var(--white);z-index:3}
.brand{position:absolute;left:265px;top:26px;display:flex;align-items:center;gap:8px;font-size:17px;font-weight:700;color:var(--ink)}
.brand-mark{width:14px;height:14px;background:var(--blue-deep)}
.main-nav{position:absolute;top:32px;left:553px;display:flex;gap:26px;font-size:11.5px;font-weight:600}
.main-nav a{color:var(--ink);text-decoration:none}

/* hero */
.hero-photo{position:absolute;left:0;top:74px;width:1200px;height:706px;
  background:radial-gradient(ellipse at 75% 45%,#c9a34a 0%,#b48a3a 22%,#d6cdb8 50%,#e4e4e0 70%,#f1ece0 100%)}
.hero-wave{position:absolute;left:0;top:74px}
.hero-copy{position:absolute;left:262px;top:314px}
.eyebrow{display:inline-block;font-size:13px;font-weight:700;color:var(--blue);border-bottom:2px solid var(--blue);padding:0 1px 2px;margin-left:3px}
.hero-title{font-size:34px;font-weight:600;line-height:42px;margin-top:14px}
.btn{display:inline-flex;align-items:center;gap:10px;font-weight:700;font-size:13px;text-decoration:none}
.btn-orange{background:var(--orange-soft);color:var(--white)}
.hero-btn{position:absolute;left:264px;top:443px;width:141px;height:31px;padding-left:21px}
.tagline{position:absolute;left:0;width:1200px;top:693px;text-align:center;color:var(--orange-soft);font-size:21px;font-weight:600;line-height:27px}

/* pillars */
.pillar h3{font-size:18px;font-weight:600;margin-top:2px}
.pillar p{font-size:12px;line-height:15px;color:var(--text);margin-top:6px}
.pillar svg{display:block}

/* services band */
.services-band{position:absolute;left:0;top:1211px;width:1200px;height:321px;background:var(--blue-soft)}
.services-title{position:absolute;left:266px;top:1268px;font-size:20px;font-weight:600;line-height:26px;color:var(--white)}
.services-title span{color:var(--blue-deep)}
.btn-outline{position:absolute;left:265px;top:1344px;width:175px;height:37px;border:1.5px solid var(--white);border-radius:19px;color:var(--white);padding-left:19px}
.band-word{position:absolute;left:530px;top:1362px;font-size:66px;font-weight:700;letter-spacing:2px;color:rgba(255,255,255,.08)}
.service-card{position:absolute;top:1431px;width:228px;height:279px}
.card-label{position:absolute;left:0;bottom:12px;width:165px;height:63px;background:rgba(255,255,255,.85);display:flex;align-items:center;padding-left:16px;font-size:14.5px;font-weight:600;line-height:18px}
.slider-arrow{position:absolute;top:1560px;width:47px;height:25px;background:var(--arrow-blue);display:flex;align-items:center;justify-content:center}

/* contact strip */
.rule{position:absolute;left:266px;width:666px;height:1px;background:#555}
.cta-title{position:absolute;left:0;width:1200px;top:1832px;text-align:center;font-size:21px;font-weight:600}
.cta-btn{position:absolute;left:521px;top:1874px;width:158px;height:32px;border-radius:16px;justify-content:center}

/* footer */
.site-footer{position:absolute;left:0;top:2020px}
.footer-links{position:absolute;left:0;width:1200px;top:2110px;text-align:center;font-size:11px;color:var(--white)}
.footer-links a{color:var(--white);text-decoration:none;margin:0 10px}
.copyright{position:absolute;left:0;width:1200px;top:2133px;text-align:center;font-size:11px;color:var(--white)}
</style>
</head>
<body>

<header class="site-header">
  <div class="brand"><span class="brand-mark"></span>Orbel Appraisals</div>
  <nav class="main-nav">
    <a href="#">Home</a><a href="#">About Us</a><a href="#">Our Services</a><a href="#">News &amp; Views</a><a href="#">Contact Us</a>
  </nav>
</header>

<div class="hero-photo" role="img" aria-label="Stacks of gold coins resting on financial newspaper pages"></div>
<svg class="hero-wave" width="1200" height="706" viewBox="0 0 1200 706" aria-hidden="true">
  <path d="M1200,354 C1110,430 1010,600 900,594 C770,588 650,490 522,501 C400,512 330,706 200,706 C120,706 50,680 0,668 L0,706 L1200,706 Z" fill="#fff"/>
</svg>

<div class="hero-copy">
  <span class="eyebrow">ORBEL APPRAISALS</span>
  <h1 class="hero-title">Business and<br>Intellectual Property Valuation</h1>
</div>
<a class="btn btn-orange hero-btn" href="#">Contact Us
  <svg width="30" height="10" viewBox="0 0 30 10"><path d="M0 5H28M23 1L28 5L23 9" stroke="#fff" stroke-width="1.4" fill="none"/></svg></a>

<p class="tagline">Trust, Service and Expertise<br>are the 3 pillars of Orbel Appraisals.</p>

<section class="pillar abs" style="left:415px;top:826px;width:222px">
  <svg width="38" height="36" viewBox="0 0 38 36" fill="none" stroke="#1a1a1a" stroke-width="1.5">
    <path d="M8 2H36V30a4 4 0 0 1-4 4H4a3 3 0 0 1-3-3V28H8Z"/><path d="M8 2v29a3 3 0 0 1-3 3"/>
    <path d="M12 10l2 2 3-3M12 18l2 2 3-3M12 26l2 2 3-3M20 11h12M20 19h12M20 27h10"/>
  </svg>
  <h3>Service</h3>
  <p>Service is front and center at Orbel Appraisals. We consider the needs of all stakeholders and the personal needs of the client team involved.</p>
</section>

<section class="pillar abs" style="left:688px;top:794px;width:246px">
  <svg width="40" height="40" viewBox="0 0 40 40" fill="none" stroke="#1a1a1a" stroke-width="1.5">
    <circle cx="22" cy="14" r="4"/><circle cx="22" cy="14" r="9" stroke-dasharray="4 3"/>
    <path d="M8 10C4 16 4 24 8 30M14 38V30M6 38l2-8"/>
  </svg>
  <h3>Expertise</h3>
  <p>Expertise is core to the philosophy of Orbel Appraisals. Our global network of professionals maintain and continue to develop the knowledge and experience that you expect from your trusted corporate finance partner.</p>
</section>

<section class="pillar abs" style="left:267px;top:1003px;width:178px">
  <svg width="34" height="38" viewBox="0 0 34 38" fill="none" stroke="#1a1a1a" stroke-width="1.6">
    <path d="M17 2L31 7V18C31 27 25 33 17 36C9 33 3 27 3 18V7Z"/><path d="M11 19l4 4 8-8"/>
  </svg>
  <h3>Trust</h3>
  <p>Trust is paramount. Clients rely on Orbel Appraisals for confidentiality, transparency and independence.</p>
</section>

<div class="services-band"></div>
<h2 class="services-title">Basically we provide 5 main<br>services at <span>Orbel Appraisals</span></h2>
<a class="btn btn-outline" href="#">View all services
  <svg width="30" height="10" viewBox="0 0 30 10"><path d="M0 5H28M23 1L28 5L23 9" stroke="#fff" stroke-width="1.4" fill="none"/></svg></a>
<div class="band-word">SERVICES</div>

<article class="service-card" style="left:248px" role="img" aria-label="Hands reviewing printed bar charts and financial reports">
  <div style="position:absolute;inset:0;background:linear-gradient(135deg,#e8edf4,#b9cde6 60%,#7ea4d4)"></div>
  <div class="card-label">Business Valuation</div>
</article>
<article class="service-card" style="left:486px" role="img" aria-label="Professional signing documents with a pen at a desk">
  <div style="position:absolute;inset:0;background:linear-gradient(120deg,#c9d3e0,#e9e6e2 50%,#c9793e)"></div>
  <div class="card-label">Intellectual Property Valuation</div>
</article>
<article class="service-card" style="left:723px" role="img" aria-label="Business partners shaking hands by an office window overlooking a city">
  <div style="position:absolute;inset:0;background:linear-gradient(180deg,#2c5f9e,#6f9fd3 55%,#1e2b40)"></div>
  <div class="card-label">M&amp;A Advisory</div>
</article>
<div class="slider-arrow" style="left:248px"><svg width="20" height="10" viewBox="0 0 20 10"><path d="M20 5H2M6 1L2 5L6 9" stroke="#fff" stroke-width="1.3" fill="none"/></svg></div>
<div class="slider-arrow" style="left:903px"><svg width="20" height="10" viewBox="0 0 20 10"><path d="M0 5H18M14 1L18 5L14 9" stroke="#fff" stroke-width="1.3" fill="none"/></svg></div>

<div class="rule" style="top:1799px"></div>
<h2 class="cta-title">Do not hesitate, to contact with us for better help and services.</h2>
<a class="btn btn-orange cta-btn" href="#">Contact Us
  <svg width="30" height="10" viewBox="0 0 30 10"><path d="M0 5H28M23 1L28 5L23 9" stroke="#fff" stroke-width="1.4" fill="none"/></svg></a>
<div class="rule" style="top:1937px"></div>

<svg class="site-footer" width="1200" height="184" viewBox="0 0 1200 184" aria-hidden="true">
  <path d="M0 64L1200 4V184H0Z" fill="#2f77b8"/>
</svg>
<nav class="footer-links"><a href="#">Home</a>|<a href="#">About</a>|<a href="#">Services</a>|<a href="#">News &amp; Views</a>|<a href="#">Contact</a></nav>
<p class="copyright">Copyright © 2019 Orbel Appraisals. All Rights Reserved</p>

</body>
</html>
```